"Made in Chicago" Baby Shower Invitation

I need a design for a baby shower invitation with the headline and theme of "Made in Chicago". The design should incorporate the colors/design of the Chicago flag. I have attached an image of the flag for your reference. The design should be sized 5-1/2 wide x 8-1/2 long. I want to be able to print two to a page on a standard 8-1/2 X 11" piece of (nice quality) paper on a standard home printer.
Copy:
Made in Chicago Baby Shower
For: Marla & Gordon
Date: Saturday, April 5, 2014
Time: 7:00 p.m.
Place: 27 West Halbrook Ave, 4B
RSVP by April 1 to Nadia Verholm/312-555-0193

Hello Designers - I corrected the size requirements of the invitation (bad math before) and added a few more notes of preference. Looking for a design that is more clean and graphic and less traditional, soft baby shower look. Thank you!

Friends & family of the 20-sometthing, urban professional couple who are having a baby.

Baby

Must have
• Chicago flag colors and/or image, the words "made in Chicago", and the (revised) size indicated.
Should not have
• Anything inappropriate or offensive to grandmother of said couple.

```html
<!DOCTYPE html>
<html lang="en">
<head>
<meta charset="utf-8">
<title>Made in Chicago – Baby Shower Invitation</title>
<link rel="stylesheet" href="https://fonts.googleapis.com/css2?family=Poppins:wght@200;300&display=swap">
<style>
  :root {
    --paper: #ffffff;
    --sky-blue: #aed4ee;
    --sky-blue-soft: #c4e0f3;
    --flag-red: #e8112d;
    --label-red: #ee4a5e;
    --ink: #2b2b2b;
  }
  * { margin: 0; padding: 0; box-sizing: border-box; }
  html, body {
    width: 776px; height: 1200px; overflow: hidden;
    background: var(--paper);
  }
  .invitation {
    position: relative; width: 776px; height: 1200px;
    background: var(--paper);
    font-family: "Poppins", "Century Gothic", sans-serif;
    font-weight: 300;
    color: var(--ink);
  }
  .skyline {
    position: absolute; left: 35px; top: 110px;
    width: 400px; height: 207px;
    background: linear-gradient(180deg, var(--sky-blue-soft), var(--sky-blue));
  }
  .rule {
    position: absolute; height: 4px; background: var(--flag-red);
  }
  .rule--top { left: 35px; top: 317px; width: 449px; }
  .rule--headline { left: 484px; top: 424px; width: 292px; }
  .headline {
    position: absolute; left: 265px; top: 340px;
    width: 475px; height: 56px; overflow: visible;
  }
  .headline text {
    font-family: "Poppins", "Century Gothic", sans-serif;
    font-weight: 200; font-size: 50px; fill: #1f1f1f;
  }
  .details-frame {
    position: absolute; left: 181px; top: 449px;
    width: 595px; height: 595px;
    border-left: 5px solid var(--sky-blue);
    border-bottom: 5px solid var(--sky-blue);
  }
  .detail {
    position: absolute; left: 0; width: 776px; line-height: 1;
  }
  .detail__label {
    position: absolute; right: 625px;
    font-size: 31px; color: var(--label-red);
    font-variant: small-caps; white-space: nowrap;
  }
  .detail__value {
    position: absolute; left: 221px;
    font-size: 30px; font-variant: small-caps;
    white-space: nowrap; color: #333;
  }
  .detail__value sup { font-size: 17px; vertical-align: 12px; line-height: 0; }
  .detail__value small {
    display: block; margin-top: 8px;
    font-size: 24px; font-variant: normal; letter-spacing: 0.5px;
  }
  .detail--for  { top: 556px; }
  .detail--date { top: 650px; }
  .detail--time { top: 745px; }
  .detail--place { top: 838px; }
  .detail--rsvp { top: 933px; }
  .star {
    position: absolute; left: 367px; top: 1094px;
    width: 42px; height: 42px;
  }
</style>
</head>
<body>
<main class="invitation">
  <div class="skyline" role="img" aria-label="Light blue city skyline illustration"></div>
  <div class="rule rule--top"></div>
  <svg class="headline" viewBox="0 0 475 56" role="heading" aria-level="1" aria-label="Made in Chicago">
    <text x="0" y="49" textLength="472" lengthAdjust="spacingAndGlyphs">MADE IN CHICAGO</text>
  </svg>
  <div class="rule rule--headline"></div>

  <section class="details-frame" aria-hidden="true"></section>

  <div class="detail detail--for">
    <span class="detail__label">For:</span>
    <span class="detail__value">Marla &amp; Gordon’s Baby Shower</span>
  </div>
  <div class="detail detail--date">
    <span class="detail__label">Date:</span>
    <span class="detail__value">Saturday, April 5, 2014</span>
  </div>
  <div class="detail detail--time">
    <span class="detail__label">Time:</span>
    <span class="detail__value">7:00 p.m.</span>
  </div>
  <div class="detail detail--place">
    <span class="detail__label">Place:</span>
    <span class="detail__value">27 West Halbrook Ave, 4B</span>
  </div>
  <div class="detail detail--rsvp">
    <span class="detail__label">RSVP:</span>
    <span class="detail__value">Nadia Verholm, By April 1<sup>st</sup><small>(312) 555-0193</small></span>
  </div>

  <svg class="star" viewBox="0 0 42 42" role="img" aria-label="Red six-pointed star">
    <polygon fill="#e8112d" points="21,0 26,12 39,10.5 31,21 39,31.5 26,30 21,42 16,30 3,31.5 11,21 3,10.5 16,12"/>
  </svg>
</main>
</body>
</html>
```